STEADFAST RECORDS, OWSG, corvendale.net, New Infographic Design Project

Corvendale.net
Infographic
See attached information
Would like charts showing where funds from each bond goes

For design inspiration only, do not copy any of the elements - https://www.plomviter.com/design/5182730

up coming Sheriffs conference! we would like something professional outlining our industries benefits to the justice process in Arkansas

see attached information. we would like similar graphics pie chart showing where money goes from each bond written etc.

Target Market(s)

Government law enforcement

Industry/Entity Type

Judicial

Requirements
Must have
• Professional graphics charts

```html
<!DOCTYPE html>
<html lang="en">
<head>
<meta charset="utf-8">
<title>Sheriffs Conference Infographic</title>
<link rel="stylesheet" href="https://fonts.googleapis.com/css2?family=Anton&family=Montserrat:wght@400;500;700;800&display=swap">
<style>
  :root{
    --navy:#0d3f86;
    --blue:#1a66b8;
    --sky:#3bb9ec;
    --cyan:#14b8d6;
    --crimson:#921f2c;
    --red:#c8101f;
    --ink:#1c1c1c;
    --text:#2b2b2b;
    --paper:#f5f5f6;
    --white:#ffffff;
  }
  *{margin:0;padding:0;box-sizing:border-box}
  html,body{width:885px;height:1200px;overflow:hidden;background:var(--paper)}
  body{position:relative;font-family:"Montserrat",Arial,sans-serif;color:var(--text)}
  .abs{position:absolute}

  .header{left:0;top:0;width:885px;height:321px;
    background:linear-gradient(180deg,#2a7ccf 0%,var(--blue) 45%,var(--navy) 100%)}
  .city-photo{left:471px;top:0;width:414px;height:321px;
    clip-path:polygon(12% 0,100% 0,100% 100%,0 100%,6% 80%,2% 60%,8% 40%,4% 20%);
    background:radial-gradient(ellipse at 70% 70%,#e8eef5 0%,#6d87a3 22%,#2c3d4e 45%,#1c2a35 70%),#1c2a35}
  .city-photo::after{content:"";position:absolute;inset:0;
    background:radial-gradient(ellipse at 40% 30%,rgba(246,170,40,.45),transparent 55%)}

  .brand{left:40px;top:46px;display:flex;align-items:center;gap:8px}
  .brand-name{font-weight:800;font-size:34px;color:var(--white);line-height:1}
  .brand-mark{width:16px;height:16px;background:var(--white)}
  .brand-sub{left:40px;top:85px;font-weight:700;font-size:11px;color:var(--white);text-transform:lowercase}

  .title{left:36px;top:120px;font-family:"Anton",Impact,sans-serif;font-size:104px;line-height:1;
    color:var(--crimson);-webkit-text-stroke:2px var(--white);paint-order:stroke fill;letter-spacing:-1px}
  .subtitle{left:38px;top:224px;font-weight:800;font-size:49px;line-height:1;color:var(--white);letter-spacing:-1px}

  .section-title{left:0;width:885px;text-align:center;font-weight:700;color:var(--crimson);line-height:1.3}
  .intro-title{top:348px;font-size:22px}
  .intro{left:40px;top:389px;width:812px;font-size:14.6px;line-height:20px;text-align:justify;color:var(--text)}

  .stat-lead{font-size:14.5px;line-height:19px;color:var(--text)}
  .stat-figure{font-weight:800;font-size:40px;line-height:1;color:var(--crimson)}
  .stat-note{font-size:10.5px;line-height:13px;color:var(--text)}

  .fees-title{top:686px;font-size:23px;line-height:31px}

  .slice-label{font-weight:700;font-size:12.2px;line-height:16px;color:var(--ink);text-transform:uppercase}
  .slice-amount{font-weight:700;font-size:10px;line-height:14px;color:var(--ink);text-transform:uppercase}
  .align-right{text-align:right}

  .total{left:0;top:1118px;width:885px;text-align:center;font-weight:800;font-size:19.5px;color:var(--ink)}
  .total .amount{color:var(--crimson)}

  .footer{left:0;top:1160px;width:885px;height:40px;background:var(--navy);
    display:flex;align-items:center;justify-content:center}
  .footer-url{font-weight:700;font-size:19px;letter-spacing:5px;color:var(--white)}
</style>
</head>
<body>

<header class="abs header"></header>
<div class="abs city-photo" role="img" aria-label="Aerial night photograph of the state capitol building among city lights"></div>

<div class="abs brand"><span class="brand-name">owsg</span><span class="brand-mark"></span></div>
<div class="abs brand-sub">ozark western surety guild</div>

<h1 class="abs title">SHERIFFS</h1>
<div class="abs subtitle">CONFERENCE!</div>

<h2 class="abs section-title intro-title">Today’s Bail Bondsman</h2>
<p class="abs intro">Arkansas is one of the only states with a regulatory licensing board and an owner funded Association with a full-time lobbyist. We work with all law enforcement agencies to secure better legislation for Arkansasand the criminal justice system.</p>

<svg class="abs" style="left:0;top:440px" width="885" height="220" viewBox="0 440 885 220">
  <defs>
    <radialGradient id="floor-shadow" cx="50%" cy="50%" r="50%">
      <stop offset="0" stop-color="#000" stop-opacity=".18"/>
      <stop offset="1" stop-color="#000" stop-opacity="0"/>
    </radialGradient>
  </defs>
  <ellipse cx="100" cy="632" rx="95" ry="10" fill="url(#floor-shadow)"/>
  <ellipse cx="380" cy="632" rx="95" ry="10" fill="url(#floor-shadow)"/>
  <ellipse cx="680" cy="632" rx="95" ry="10" fill="url(#floor-shadow)"/>
  <!-- bar one -->
  <polygon points="40,601 89,616 89,637 40,622" fill="#1566a8"/>
  <polygon points="89,616 138,601 138,622 89,637" fill="#1f86c8"/>
  <polygon points="40,601 89,587 138,601 89,616" fill="var(--sky)"/>
  <!-- bar two -->
  <polygon points="319,534 368,549 368,637 319,622" fill="#1566a8"/>
  <polygon points="368,549 417,534 417,622 368,637" fill="#1f86c8"/>
  <polygon points="319,534 368,520 417,534 368,549" fill="var(--sky)"/>
  <!-- bar three -->
  <polygon points="620,485 669,500 669,637 620,622" fill="#1566a8"/>
  <polygon points="669,500 719,485 719,622 669,637" fill="#1f86c8"/>
  <polygon points="620,485 669,471 719,485 669,500" fill="var(--sky)"/>
</svg>

<div class="abs" style="left:155px;top:546px">
  <div class="stat-lead">Our Industry<br>Maintains a</div>
  <div class="stat-figure">2.4%</div>
  <div class="stat-note" style="margin-top:2px">Failure To Appear Rate.</div>
</div>
<div class="abs" style="left:436px;top:523px">
  <div class="stat-lead">All Other forms of<br>pre-trial release<br>average a</div>
  <div class="stat-figure" style="margin-top:4px">40%</div>
  <div class="stat-note" style="margin-top:2px">Failure To Appear Rate.</div>
</div>
<div class="abs" style="left:738px;top:525px">
  <div class="stat-lead">We are</div>
  <div class="stat-figure" style="margin-top:-2px">100%</div>
  <div class="stat-note" style="margin-top:4px">Responsible for<br>extradition fees on our<br>clients with no cost to<br>the taxpayer.</div>
</div>

<h2 class="abs section-title fees-title">Legislativity Mandated Fees Collected For Every Bond<br>Executed By The Bondsman</h2>

<svg class="abs" style="left:0;top:800px" width="885" height="300" viewBox="0 800 885 300">
  <defs>
    <linearGradient id="g-state" x1="0" y1="0" x2="1" y2="0"><stop offset="0" stop-color="#12c0d4"/><stop offset="1" stop-color="#0d9be0"/></linearGradient>
    <linearGradient id="g-sheriff" x1="0" y1="0" x2="1" y2="0"><stop offset="0" stop-color="#2a9ee0"/><stop offset="1" stop-color="#1565ad"/></linearGradient>
    <linearGradient id="g-defend" x1="0" y1="0" x2="1" y2="1"><stop offset="0" stop-color="#9c1e2c"/><stop offset="1" stop-color="#7d1320"/></linearGradient>
    <linearGradient id="g-child" x1="1" y1="0" x2="0" y2="1"><stop offset="0" stop-color="#0b3f86"/><stop offset="1" stop-color="#1a6ec8"/></linearGradient>
    <linearGradient id="g-bail" x1="0" y1="0" x2="1" y2="0"><stop offset="0" stop-color="#d40f22"/><stop offset="1" stop-color="#8c0a16"/></linearGradient>
  </defs>

  <!-- leader lines -->
  <g fill="none" stroke-width="1.3">
    <polyline points="413,873 413,823 581,823" stroke="var(--cyan)"/>
    <line x1="593" y1="901" x2="823" y2="901" stroke="var(--blue)"/>
    <line x1="63" y1="921" x2="300" y2="921" stroke="var(--red)"/>
    <polyline points="377,1047 377,1073 63,1073" stroke="var(--blue)"/>
    <line x1="521" y1="1043" x2="823" y2="1043" stroke="var(--crimson)"/>
  </g>
  <circle cx="581" cy="823" r="3.5" fill="var(--cyan)"/>
  <circle cx="823" cy="901" r="3.5" fill="var(--blue)"/>
  <circle cx="63" cy="921" r="3.5" fill="var(--red)"/>
  <circle cx="63" cy="1073" r="3.5" fill="var(--blue)"/>
  <circle cx="823" cy="1043" r="3.5" fill="var(--crimson)"/>

  <!-- pie depth -->
  <g transform="translate(438,975) scale(1,0.42)">
    <path d="M0 0 L180.3 15.8 A181 181 0 0 1 -15.8 180.3 Z" fill="#6a0f1a"/>
    <path d="M0 0 L-15.8 180.3 A181 181 0 0 1 -178.3 -31.4 Z" fill="#0f5fc0"/>
    <path transform="translate(10,-8)" d="M0 0 L128 -128 A181 181 0 0 1 180.3 15.8 Z" fill="#1a78c4"/>
    <path transform="translate(-12,-6)" d="M0 0 L-178.3 -31.4 A181 181 0 0 1 -76.5 -164 Z" fill="#a10d1b"/>
  </g>
  <!-- pie top -->
  <g transform="translate(438,949) scale(1,0.42)">
    <path d="M0 0 L-76.5 -164 A181 181 0 0 1 128 -128 Z" fill="url(#g-state)"/>
    <path d="M0 0 L180.3 15.8 A181 181 0 0 1 -15.8 180.3 Z" fill="url(#g-defend)"/>
    <path d="M0 0 L-15.8 180.3 A181 181 0 0 1 -178.3 -31.4 Z" fill="url(#g-child)"/>
    <path transform="translate(10,-8)" d="M0 0 L128 -128 A181 181 0 0 1 180.3 15.8 Z" fill="url(#g-sheriff)"/>
    <path transform="translate(-12,-6)" d="M0 0 L-178.3 -31.4 A181 181 0 0 1 -76.5 -164 Z" fill="url(#g-bail)"/>
  </g>
</svg>

<div class="abs" style="left:436px;top:802px">
  <div class="slice-label">State General Revenue<br>&amp; Agency Operation</div>
  <div class="slice-amount" style="margin-top:12px">$6.00 per bond</div>
</div>
<div class="abs" style="left:648px;top:864px">
  <div class="slice-label">Ridgeview<br>Sheriffs’ Alliance</div>
  <div class="slice-amount" style="margin-top:7px">$6.00 per bond 100% of the<br>budget</div>
</div>
<div class="abs align-right" style="left:45px;top:865px;width:200px">
  <div class="slice-label">Bail Bond Recovery<br>Fund (Paid to the<br>County General Fund)</div>
  <div class="slice-amount" style="margin-top:10px">$4.00 per bond</div>
</div>
<div class="abs align-right" style="left:45px;top:1018px;width:200px">
  <div class="slice-label">Halvern Family<br>Safety<br>Commission</div>
  <div class="slice-amount" style="margin-top:10px">$4.00 per bond</div>
</div>
<div class="abs" style="left:648px;top:1004px">
  <div class="slice-label">Halvern Public<br>Defenders Commission</div>
  <div class="slice-amount" style="margin-top:11px">$20.00 per bond&nbsp; 2/3 of their<br>budget</div>
</div>

<div class="abs total">TOTAL REVENUE GENERATED IN 2019 PRE-COVID <span class="amount">$3,476,160.00</span></div>

<footer class="abs footer"><span class="footer-url">WWW.CORVENDALE.NET</span></footer>

</body>
</html>
```